Kelvora Power

We need a business card for "Kelvora power". I have uploaded the logo, the color of the card should be according to the logo "Blackish".
Basically kelvora power is a solar company.
Also we would like a sample file in which we can edit the information such names and contact details ourselves
The card would be two sided with following details
1- logo on front and underneath the logo there should be a line saying
"Cleaner . Cheaper . Power"
2-website i.e "www.kelvorapower.example"
3- Icons for Facebook and Instagram that tells the clients we are available on both social sites.
4- name of the person with his/her designation underneath and email address
5-contact number
6- 1-800--- number with the extension number

its up to the designer how he/she places the details,but it must look professional

5-contact number

Requirements
Must have
• 1- logo on front and underneath the logo there should be a line saying
• "Cleaner . Cheaper . Power"
• 2-website i.e "www.kelvorapower.example"
• 3- Icons for Facebook and Instagram that tells the clients we are available on both social sites.
• 4- name of the person with his/her designation underneath and email address
• 5-contact number of the person
• 6- 1-800--- number with the extension number
• 7-card should be in black shade like the logo

```html
<!DOCTYPE html>
<html lang="en">
<head>
<meta charset="utf-8">
<title>Kelvora Power – Business Card</title>
<link href="https://fonts.googleapis.com/css2?family=Open+Sans:wght@400;600;700&display=swap" rel="stylesheet">
<style>
  :root {
    --page-bg: #3a322e;
    --card-bg: #161616;
    --card-edge: #222222;
    --brand-green: #7cc142;
    --text-light: #f2f2f2;
    --text-muted: #9a9a9a;
    --divider: #5a5a5a;
  }
  * { box-sizing: border-box; margin: 0; padding: 0; }
  html, body {
    width: 1200px; height: 864px; overflow: hidden;
    background: var(--page-bg);
    font-family: "Open Sans", Arial, sans-serif;
  }
  .canvas {
    position: relative; width: 1200px; height: 864px;
  }
  .card {
    position: absolute; left: 280px; width: 640px; height: 366px;
    background: var(--card-bg);
    border: 1px solid var(--card-edge);
    border-radius: 4px;
    box-shadow: 0 10px 30px rgba(0,0,0,.45);
  }
  .card--back { top: 38px; }
  .card--front { top: 460px; }

  /* Back side */
  .back-logo {
    position: absolute; left: 0; right: 0; top: 130px;
    display: flex; justify-content: center; align-items: center; gap: 14px;
  }
  .brand-dot {
    width: 34px; height: 34px; border-radius: 50%;
    background: var(--brand-green);
  }
  .brand-name {
    font-weight: 700; color: var(--brand-green);
    font-size: 40px; letter-spacing: .5px; line-height: 1;
  }
  .back-website {
    position: absolute; left: 0; right: 0; top: 232px;
    text-align: center; color: var(--text-muted);
    font-size: 15px; letter-spacing: 4px;
  }

  /* Front side */
  .front-logo {
    position: absolute; left: 46px; top: 140px; width: 290px;
  }
  .front-logo .brand-row { display: flex; align-items: center; gap: 10px; }
  .front-logo .brand-dot { width: 26px; height: 26px; }
  .front-logo .brand-name { font-size: 30px; }
  .tagline {
    margin-top: 10px; margin-left: 36px;
    color: var(--text-light); font-size: 14px; letter-spacing: .3px;
  }
  .front-divider {
    position: absolute; left: 352px; top: 110px;
    width: 1px; height: 150px; background: var(--divider);
  }
  .contact {
    position: absolute; left: 376px; top: 130px;
  }
  .person-name {
    color: var(--brand-green); font-weight: 700; font-size: 20px; line-height: 1.1;
  }
  .person-title {
    color: var(--text-muted); font-size: 14px; margin-bottom: 14px;
  }
  .contact-list { list-style: none; }
  .contact-list li {
    display: flex; align-items: center; gap: 9px;
    color: var(--text-light); font-size: 15px; line-height: 24px;
  }
  .contact-list svg { width: 14px; height: 14px; flex: none; }
  .social {
    position: absolute; right: 22px; top: 22px; display: flex; gap: 6px;
  }
  .social-badge {
    width: 16px; height: 16px; border-radius: 2px; background: var(--brand-green);
  }
</style>
</head>
<body>
<div class="canvas">

  <section class="card card--back" aria-label="Business card back">
    <div class="back-logo">
      <span class="brand-dot"></span>
      <span class="brand-name">Kelvora Power</span>
    </div>
    <p class="back-website">www.kelvorapower.example</p>
  </section>

  <section class="card card--front" aria-label="Business card front">
    <div class="social" aria-label="Social profiles">
      <span class="social-badge"></span>
      <span class="social-badge"></span>
    </div>

    <div class="front-logo">
      <div class="brand-row">
        <span class="brand-dot"></span>
        <span class="brand-name">Kelvora Power</span>
      </div>
      <p class="tagline">Cleaner . Cheaper . Power</p>
    </div>

    <div class="front-divider"></div>

    <div class="contact">
      <p class="person-name">MARA LINDQVIST</p>
      <p class="person-title">PRESIDENT</p>
      <ul class="contact-list">
        <li>
          <svg viewBox="0 0 16 16" aria-hidden="true"><path fill="#7cc142" d="M3.6 1.5l2.3 2.6-1.4 1.6c.9 2 2.6 3.8 4.7 4.8l1.6-1.4 2.7 2.3-1.3 2.4C7.2 13.5 2.2 8.6 1.3 2.8z"/></svg>
          1-800-5550-1472
        </li>
        <li>
          <svg viewBox="0 0 16 16" aria-hidden="true"><rect x="1" y="3" width="14" height="10" rx="1.5" fill="#7cc142"/><path d="M1.8 4l6.2 5 6.2-5" fill="none" stroke="#161616" stroke-width="1.3"/></svg>
          mara@kelvorapower.example
        </li>
        <li>
          <svg viewBox="0 0 16 16" aria-hidden="true"><circle cx="8" cy="8" r="6.5" fill="none" stroke="#7cc142" stroke-width="1.6"/><path d="M1.5 8h13M8 1.5c-3 3.5-3 9.5 0 13M8 1.5c3 3.5 3 9.5 0 13" fill="none" stroke="#7cc142" stroke-width="1.2"/></svg>
          www.kelvorapower.example
        </li>
      </ul>
    </div>
  </section>

</div>
</body>
</html>
```